バリエーション多く提案していただき採用させていただきました。
自分の意図している事を非常に再現性高く提案していただきありがとうございます。
ご応募いただきありがとうございます。今後も募集しますので何卒宜しくお願いします。
恋愛学習コンテンツの動画サムネイル バナー作成の仕事の依頼
女性的 男性的
希望する色 特になし・その他 追記事項: カテゴリごとに色変えてほしい
特記事項
• 継続依頼あり
• 参考記事URL
https://palvento-mirai.example/korunade

```html
<!DOCTYPE html>
<html lang="ja">
<head>
<meta charset="utf-8">
<title>会話術｜「この人いいな」思わせる方法3選</title>
<link rel="stylesheet" href="https://fonts.googleapis.com/css2?family=Noto+Serif+JP:wght@900&family=Noto+Sans+JP:wght@900&display=swap">
<style>
  :root {
    --paper: #ffffff;
    --ink: #111111;
    --band: #9a9a9a;
    --dot: #ffffff;
  }
  * { margin: 0; padding: 0; box-sizing: border-box; }
  html, body { width: 1200px; height: 676px; overflow: hidden; background: var(--paper); }
  .thumbnail {
    position: relative;
    width: 1200px;
    height: 676px;
    background: var(--paper);
    overflow: hidden;
    font-family: "Noto Serif JP", serif;
    font-weight: 900;
    color: var(--ink);
  }
  .footer-band {
    position: absolute;
    left: 0; right: 0; bottom: 0;
    height: 140px;
    background: var(--band);
  }
  .dot-row {
    position: absolute;
    left: 296px;
    top: 560px;
    display: flex;
    gap: 24px;
  }
  .dot-row span {
    width: 80px; height: 80px;
    border-radius: 50%;
    background: var(--dot);
  }
  .category-ribbon {
    position: absolute;
    left: 24px; top: 0;
    width: 172px; height: 604px;
  }
  .category-label {
    position: absolute;
    left: 24px; top: 52px;
    width: 172px;
    display: flex;
    flex-direction: column;
    align-items: center;
    gap: 70px;
    font-family: "Noto Sans JP", sans-serif;
    font-size: 82px;
    line-height: 1;
    color: var(--paper);
  }
  .headline-quote {
    position: absolute;
    left: 262px; top: 40px;
    font-size: 118px;
    line-height: 1;
    letter-spacing: -4px;
    white-space: nowrap;
  }
  .headline-big {
    position: absolute;
    left: 276px; top: 252px;
    font-size: 240px;
    line-height: 1;
  }
  .headline-stack {
    position: absolute;
    left: 528px; top: 258px;
    font-size: 104px;
    line-height: 1;
    white-space: nowrap;
  }
  .headline-stack .lower {
    display: block;
    margin-top: 10px;
    letter-spacing: 12px;
  }
  .headline-count {
    position: absolute;
    left: 798px; top: 268px;
    font-size: 204px;
    line-height: 1;
    letter-spacing: -8px;
    white-space: nowrap;
  }
  .headline-count .unit { font-size: 180px; }
</style>
</head>
<body>
  <main class="thumbnail">
    <div class="footer-band"></div>
    <div class="dot-row" aria-hidden="true">
      <span></span><span></span><span></span><span></span>
      <span></span><span></span><span></span><span></span>
    </div>

    <svg class="category-ribbon" viewBox="0 0 172 604" aria-hidden="true">
      <polygon points="0,0 172,0 172,604 86,544 0,604" fill="var(--ink)"/>
    </svg>
    <div class="category-label"><span>会</span><span>話</span><span>術</span></div>

    <h1>
      <span class="headline-quote">「この人いいな」</span>
      <span class="headline-big">思</span>
      <span class="headline-stack">わせる<span class="lower">方法</span></span>
      <span class="headline-count">3<span class="unit">選</span></span>
    </h1>
  </main>
</body>
</html>
```